Kova upkeep RT Sun Systems

Solar power system install
Services and maintenance
wiring, Rewinding and Renovation
Switch Board Upgrade
Power and lighting point
t doesn’t matter how much you spend on quality parts, your solar system will let you down if your design and installation are sub-par. Have your solar system tailored and installed by our Master Electrician and Bright Power Guild Accredited team.

Target Market(s)

sales and installed

Industry/Entity Type

Solar install and retailer

Contact Information for Business Card

Name , Email, Phone Number ,Business address,

Font styles to use
Serif

Colors
0054AA
0677BA
7BADD7
CADEEF
E8F1F8

Requirements
Must have
• clear and bright
Nice to have
• new design
Should not have
• unclear pictures

```html
<!DOCTYPE html>
<html lang="en">
<head>
<meta charset="utf-8">
<title>Kova upkeep – Business Card</title>
<link href="https://fonts.googleapis.com/css2?family=Lato:wght@400;700;900&display=swap" rel="stylesheet">
<style>
  :root {
    --ink: #231f20;
    --blue: #0f56a8;
    --white: #ffffff;
    --grey-line: #8a8a8a;
    --text-dark: #1e1e1e;
    --stage: #e9ebee;
  }
  * { box-sizing: border-box; margin: 0; padding: 0; }
  html, body { width: 1200px; height: 895px; overflow: hidden; }
  body {
    background: var(--stage);
    font-family: "Lato", sans-serif;
    position: relative;
  }
  .card {
    position: absolute;
    top: 287px;
    width: 560px;
    height: 320px;
    overflow: hidden;
    box-shadow: 0 4px 14px rgba(0,0,0,0.18);
  }
  .card--front { left: 20px; background: var(--ink); }
  .card--back { left: 620px; background: var(--white); }

  /* brand lockup */
  .brand { display: flex; flex-direction: column; align-items: center; }
  .brand__mark {
    width: 34px; height: 34px; background: var(--blue); margin-bottom: 10px;
  }
  .brand__name {
    font-weight: 900; font-size: 30px; letter-spacing: 0.5px; line-height: 1;
  }
  .brand__tag {
    font-weight: 700; font-size: 15px; letter-spacing: 1.5px; color: var(--blue);
    margin-top: 5px;
  }

  .card--front .brand { position: absolute; top: 44px; left: 0; right: 0; }
  .card--front .brand__name { color: var(--white); }
  .front__rule {
    position: absolute; top: 170px; left: 120px; width: 320px; height: 1px;
    background: var(--grey-line);
  }
  .services {
    position: absolute; top: 190px; left: 22px; right: 22px;
    list-style: none; display: grid;
    grid-template-columns: auto auto auto; justify-content: space-between;
    column-gap: 10px; row-gap: 10px;
    color: var(--white); font-size: 11.5px;
  }
  .services li { display: flex; align-items: center; white-space: nowrap; }
  .services li::before {
    content: ""; width: 9px; height: 7px; background: var(--blue);
    margin-right: 6px; transform: skewX(-20deg); flex: none;
  }
  .front__band {
    position: absolute; left: 0; right: 0; bottom: 10px; height: 10px;
    background: var(--blue);
  }

  .card--back .brand { position: absolute; top: 90px; left: 30px; width: 260px; }
  .card--back .brand__name { color: var(--text-dark); font-size: 28px; }
  .back__divider {
    position: absolute; top: 60px; left: 305px; width: 1px; height: 170px;
    background: var(--text-dark);
  }
  .contact { position: absolute; top: 62px; left: 325px; color: var(--text-dark); }
  .contact__name {
    font-weight: 900; font-size: 21px; color: var(--blue); letter-spacing: 0.3px;
  }
  .contact__role { font-size: 13.5px; margin-top: 1px; }
  .contact__address { font-size: 13.5px; line-height: 1.3; margin-top: 18px; }
  .contact__lines { list-style: none; margin-top: 16px; font-size: 13.5px; }
  .contact__lines li { display: flex; align-items: center; gap: 8px; line-height: 1.5; }
  .contact__lines svg { width: 12px; height: 12px; fill: var(--blue); flex: none; }
  .back__strip {
    position: absolute; left: 0; right: 0; bottom: 0; height: 10px;
    background: var(--ink);
  }
</style>
</head>
<body>

<section class="card card--front">
  <div class="brand">
    <span class="brand__mark"></span>
    <span class="brand__name">KOVA UPKEEP</span>
    <span class="brand__tag">RT SUN SYSTEMS</span>
  </div>
  <div class="front__rule"></div>
  <ul class="services">
    <li>Solar power system install</li>
    <li>Services and maintenance wiring</li>
    <li>Power and lighting point</li>
    <li>Rewinding and Renovation</li>
    <li>Switch Board Upgrade</li>
  </ul>
  <div class="front__band"></div>
</section>

<section class="card card--back">
  <div class="brand">
    <span class="brand__mark"></span>
    <span class="brand__name">KOVA UPKEEP</span>
    <span class="brand__tag">RT SUN SYSTEMS</span>
  </div>
  <div class="back__divider"></div>
  <div class="contact">
    <p class="contact__name">DANIEL HARPER</p>
    <p class="contact__role">Founder &amp; CEO</p>
    <p class="contact__address">42 Fenwick Row, London<br>LN4 7QT</p>
    <ul class="contact__lines">
      <li><svg viewBox="0 0 24 24"><path d="M6.6 10.8a15.1 15.1 0 0 0 6.6 6.6l2.2-2.2a1 1 0 0 1 1-.25 11.4 11.4 0 0 0 3.6.57 1 1 0 0 1 1 1V20a1 1 0 0 1-1 1A17 17 0 0 1 3 4a1 1 0 0 1 1-1h3.5a1 1 0 0 1 1 1c0 1.25.2 2.450.57 3.570a1 1 0 0 1-.25 1z"/></svg>555 018 2246</li>
      <li><svg viewBox="0 0 24 24"><path d="M2 5h20v2l-10 6L2 7z"/><path d="M2 9l10 6 10-6v10H2z"/></svg>info@kovaupkeep.com</li>
      <li><svg viewBox="0 0 24 24"><path d="M12 2a10 10 0 1 0 0 20 10 10 0 0 0 0-20zm6.9 6h-3a15.6 15.6 0 0 0-1.3-3.9A8 8 0 0 1 18.9 8zM12 4c.8 1.1 1.5 2.5 1.9 4h-3.8c.4-1.5 1.1-2.9 1.9-4zM4.3 14a8 8 0 0 1 0-4h3.4a16 16 0 0 0 0 4zm.8 2h3a15.6 15.6 0 0 0 1.3 3.9A8 8 0 0 1 5.1 16zM8 8H5.1a8 8 0 0 1 4.3-3.9A15.6 15.6 0 0 0 8 8zm4 12c-.8-1.1-1.5-2.5-1.9-4h3.8c-.4 1.5-1.1 2.9-1.9 4zm2.3-6H9.7a14.6 14.6 0 0 1 0-4h4.6a14.6 14.6 0 0 1 0 4zm.3 5.9A15.6 15.6 0 0 0 15.9 16h3a8 8 0 0 1-4.3 3.9zM16.3 14a16 16 0 0 0 0-4h3.4a8 8 0 0 1 0 4z"/></svg>www.kovaupkeep.com</li>
    </ul>
  </div>
  <div class="back__strip"></div>
</section>

</body>
</html>
```